B2B telecom company need web design

We need a web design for our corporate web site. The company exists since almost 10 years.
This is a DESIGN contest, you're expected to provide design only, NOT the whole website. The winner will have to provide the HTML template (with Lorem Ipsum content) and the CSS files of his design.
Our initial product is SMS peering in P2P (you send a SMS to a friend in a foreign country, great chance that your operator route your SMS to us that we route to the recipient). We're launching a bulk SMS service (marketing and application to SMS).
Target is mostly corporate, usually big corporate (operators, contents providers...) where use of SMS is part of the main business.
The web site is composed of 1 landing page and 7 content pages (plan is given for your information, all content page are using the same template and the same design, you do NOT need to make one design per page) :
* About US
Company Profile
They trust us
The Volnor Team
Partners
Contact us
* Solution
P2P SMS
A2P SMS
You only need to submit the landing page and a template page for the content (with h1, h2, h3 and h4).
Design must be based on our new logo (see attached file).
Our current web site http://www.volnor-example.com
The winner of the contest will have to provide state of the art HTML template and CSS files of his design. Photo used shall be downloaded from Pixelbrook (provide the ID of the picture that we purchase file).
Target Market(s)
Telecom operator. SMS Peering hubs. Bulk SMS.
Industry/Entity Type
It Company
Number of Pages Required
2 page

```html
<!DOCTYPE html>
<html lang="en">
<head>
<meta charset="utf-8">
<title>Volnor Mobile Exchange</title>
<link rel="stylesheet" href="https://fonts.googleapis.com/css2?family=Bebas+Neue&family=Arimo:wght@400;700&display=swap">
<style>
:root{
  --green:#9ccc2a;
  --green-text:#8dc21f;
  --ink:#4a4a4a;
  --muted:#777;
  --light-bg:#f6f6f6;
  --line:#e3e3e3;
}
*{margin:0;padding:0;box-sizing:border-box}
html,body{width:1200px;height:1000px;overflow:hidden;background:#fff}
body{position:relative;font-family:"Arimo",Arial,sans-serif;color:var(--muted)}
.abs{position:absolute}
.display{font-family:"Bebas Neue",Impact,sans-serif;font-weight:400}

/* header */
.site-header{left:0;top:0;width:1200px;height:56px;background:#fff;z-index:2}
.brand{left:231px;top:14px;font-size:23px;color:var(--ink);letter-spacing:.5px;line-height:28px;z-index:3;white-space:nowrap}
.main-nav{left:687px;top:24px;display:flex;font-size:10px;color:#555;list-style:none;z-index:3}
.main-nav li{padding:0 14px;border-left:1px solid #ccc;line-height:12px}
.main-nav li:first-child{border-left:none}
.main-nav .current{color:var(--green-text)}
.header-shadow{left:430px;top:50px;width:360px;height:14px;border-radius:50%;
  box-shadow:0 6px 8px rgba(0,0,0,.22);z-index:1}

/* hero */
.hero{left:0;top:56px;width:1200px;height:315px;background:var(--light-bg)}
.hero-map{left:205px;top:100px;width:462px;height:246px;z-index:2}
.hero-title{left:701px;top:174px;font-size:23px;color:#555;line-height:26px;z-index:2;white-space:nowrap}
.hero-subtitle{left:701px;top:204px;font-size:15px;color:var(--green-text);z-index:2}
.hero-text{left:700px;top:235px;width:290px;font-size:11.5px;color:#555;line-height:15px;z-index:2}
.hero-text em{font-style:normal;color:var(--green-text)}

/* ticker */
.ticker{left:0;top:371px;width:1200px;height:35px;background:#fff;border-bottom:1px solid var(--green)}
.ticker-item{top:382px;font-size:10px;color:#555;white-space:nowrap;line-height:13px}
.ticker-dot{top:386px;width:5px;height:5px;border-radius:50%;background:var(--green)}
.ticker-arrow{top:383px}

/* welcome */
.welcome-title{left:10px;width:1200px;top:481px;text-align:center;font-size:20px;color:var(--muted)}
.welcome-copy{left:320px;width:580px;top:521px;text-align:center;font-size:10px;line-height:15px;color:var(--muted)}
.welcome-copy p+p{margin-top:15px}

/* features */
.features{left:0;top:677px;width:1200px;height:244px;background:var(--light-bg);border-top:1px solid #ececec}
.feature{top:733px}
.feature h3{font-family:"Bebas Neue",Impact,sans-serif;font-weight:400;font-size:16px;color:var(--ink);margin-bottom:18px;white-space:nowrap}
.feature .lead{font-size:11.5px;line-height:15.5px;color:var(--green-text)}
.feature .date{font-size:9.5px;color:#999;display:flex;align-items:center;gap:5px;margin-bottom:3px}
.feature .note{font-size:9px;line-height:13px;color:#555;margin-top:8px}
.read-more{display:inline-block;font-size:10px;color:#555;text-decoration:underline;margin-top:12px}

/* footer */
.site-footer{left:0;top:921px;width:1200px;height:79px;background:#fff;border-top:1px solid var(--line)}
.footer-brand{left:231px;top:955px;font-size:18px;color:#9a9a9a;white-space:nowrap}
.footer-legal{left:447px;top:958px;font-size:8.5px;color:#888;white-space:nowrap}
.footer-legal span{margin:0 3px}
</style>
</head>
<body>

<header class="site-header abs"></header>
<div class="brand abs">VOLNOR mobile</div>
<ul class="main-nav abs">
  <li class="current">home</li>
  <li>about us</li>
  <li>solutions</li>
  <li>news</li>
  <li>contact us</li>
</ul>
<div class="header-shadow abs"></div>

<section class="hero abs"></section>
<svg class="hero-map abs" role="img" aria-label="World map in grey with Europe, Africa and the Middle East highlighted in green" viewBox="0 0 462 246">
  <defs>
    <linearGradient id="mapTone" x1="0" x2="1" y1="0" y2="0">
      <stop offset="0" stop-color="#a3a3a3"/>
      <stop offset="0.45" stop-color="#a3a3a3"/>
      <stop offset="0.5" stop-color="#a6d42a"/>
      <stop offset="0.62" stop-color="#a6d42a"/>
      <stop offset="0.68" stop-color="#a3a3a3"/>
    </linearGradient>
  </defs>
  <rect width="462" height="246" rx="6" fill="url(#mapTone)" opacity="0.55"/>
</svg>
<h1 class="hero-title abs display">Africa &amp; Middle East Exchange</h1>
<h2 class="hero-subtitle abs display">Marketing and Application to SMS</h2>
<p class="hero-text abs display">Lorem ipsum dolor sit amet, consectetur <em>adipiscing elit</em>, sed do eiusmod tempor incididunt ut labore et dolore magna aliqua.</p>

<div class="ticker abs"></div>
<svg class="ticker-arrow abs" style="left:227px" width="8" height="12" viewBox="0 0 8 12"><path d="M7 1 2 6l5 5" fill="none" stroke="#9ccc2a" stroke-width="1.4"/></svg>
<span class="ticker-item abs" style="left:246px">120+ Premium Connections</span>
<span class="ticker-dot abs" style="left:372px"></span>
<span class="ticker-item abs" style="left:387px">1000 Global Companies</span>
<span class="ticker-dot abs" style="left:498px"></span>
<span class="ticker-item abs" style="left:513px">500+ Operator Connected</span>
<span class="ticker-dot abs" style="left:632px"></span>
<span class="ticker-item abs" style="left:647px">Massaging You can Count on</span>
<span class="ticker-dot abs" style="left:778px"></span>
<span class="ticker-item abs" style="left:791px">365 Days a Year</span>
<span class="ticker-dot abs" style="left:868px"></span>
<span class="ticker-item abs" style="left:882px">5 Global Data Centers</span>
<svg class="ticker-arrow abs" style="left:987px" width="8" height="12" viewBox="0 0 8 12"><path d="M1 1l5 5-5 5" fill="none" stroke="#999" stroke-width="1.4"/></svg>

<h2 class="welcome-title abs display">Welcome to Volnor !</h2>
<div class="welcome-copy abs">
  <p>VOLNOR Mobile Exchange is the combination of world-class enterprise solutions and an unrivaled global data network, creating the world's foremost provider of mobile enterprise applications and messaging. The result for our customers is unlimited potential.</p>
  <p>VOLNOR Mobile Exchange with his Partners , has the resources, presence, knowledge, and experience to make any mobile strategy come to life. No other company comes close in terms of global reach, mobile enterprise software and services, or industry experience. VOLNOR Mobile Exchange delivers messages to the point of action—helping customers get serious about mobile.</p>
</div>

<section class="features abs"></section>
<article class="feature abs" style="left:228px;width:205px">
  <h3>Whats New</h3>
  <div class="date"><svg width="10" height="10" viewBox="0 0 10 10"><circle cx="5" cy="5" r="4" fill="none" stroke="#999" stroke-width="1.2"/><path d="M5 2.8V5h1.8" fill="none" stroke="#999"/></svg>20 May 2014</div>
  <p class="lead">Tellway 365 consolidates reach into</p>
  <p class="note">Tellway 365 consolidation into Africa ANd Middle Eastwith new reagnal Mobile Massaging HUB</p>
  <a class="read-more">Read More</a>
</article>
<article class="feature abs" style="left:449px;width:180px">
  <h3>Mobile Advantage</h3>
  <p class="lead">VOLNOR Mobile Exchange leads the world in the delivery, billing, and settlement of mobile messaging services.</p>
  <a class="read-more">Read More</a>
</article>
<article class="feature abs" style="left:641px;width:180px">
  <h3>Mobile Interoperability</h3>
  <p class="lead">VOLNOR Mobile Exchange is the global leader in mobile interoper-ability messaging using both IP and SS7.</p>
  <a class="read-more">Read More</a>
</article>
<article class="feature abs" style="left:832px;width:180px">
  <h3>Mobile Solutions</h3>
  <p class="lead">VOLNOR Mobile Exchange leads the world in the delivery, billing, and settlement of mobile messaging services.</p>
  <a class="read-more">Read More</a>
</article>

<footer class="site-footer abs"></footer>
<div class="footer-brand abs">VOLNOR mobile</div>
<p class="footer-legal abs">©2015 VOLNOR Mobile Exchange. &nbsp; Privacy Policy<span>|</span>Legal Use<span>|</span>Anti-Spam Policy<span>|</span>Site Map</p>

</body>
</html>
```